Geothermal company needs a creative "POW" business card

Manufacturers tend to be boring. We are not! We are a Geothermal Heat Pump company that has over 30 yrs of experience and wants a new look and updated feel. Nothing old (yawn) so get your creative hats on and let's rock!

We want to use the great colors of lime green and navy blue. Our new logo is attached and we're ready to roll. Remember, we're a professional leader in the geothermal industry that needs to make an eye catching and memorable first glance.

```html
<!DOCTYPE html>
<html lang="en">
<head>
<meta charset="utf-8">
<title>Borealis Thermal – Business Card</title>
<link rel="stylesheet" href="https://fonts.googleapis.com/css2?family=Open+Sans:wght@400;600;700&display=swap">
<style>
  :root{
    --lime:#7dbb36;
    --green-dark:#2f8a34;
    --navy:#1d3f7a;
    --ink:#3a3a3a;
    --card:#ffffff;
    --stage:#e9e9ec;
  }
  *{box-sizing:border-box;margin:0;padding:0}
  html,body{width:1200px;height:987px;overflow:hidden}
  body{background:var(--stage);font-family:"Open Sans",Arial,sans-serif;position:relative}
  .card{position:absolute;width:640px;height:366px;background:var(--card);border-radius:24px;box-shadow:0 6px 18px rgba(0,0,0,.15);overflow:hidden}
  .card--front{left:280px;top:90px}
  .card--back{left:280px;top:530px}

  .brand{position:absolute;left:40px;top:38px;display:flex;align-items:center;gap:16px}
  .brand__dot{width:64px;height:64px;border-radius:50%;background:var(--navy)}
  .brand__name{font-size:44px;font-weight:700;color:var(--lime);line-height:1;letter-spacing:-.5px;white-space:nowrap}
  .tagline{position:absolute;left:120px;top:96px;font-size:15px;color:var(--navy);font-weight:600;white-space:nowrap}

  .person{position:absolute;left:40px;top:128px;font-size:24px;color:var(--lime);font-weight:600}
  .person__role{color:var(--navy);font-size:18px;font-weight:400}
  .contacts{position:absolute;left:40px;top:170px;list-style:none;font-size:16px;color:var(--ink);line-height:27px}
  .contacts li{display:flex;align-items:center;gap:10px}
  .contacts svg{width:16px;height:16px;fill:var(--lime)}

  .web-band{position:absolute;left:0;top:268px;width:100%;height:38px;background:linear-gradient(90deg,var(--green-dark),var(--lime));color:#fff;font-size:18px;letter-spacing:1px;padding-left:40px;line-height:38px}
  .address{position:absolute;left:40px;top:318px;font-size:16px;color:var(--ink)}

  .back-mark{position:absolute;left:0;right:0;top:92px;display:flex;flex-direction:column;align-items:center;gap:14px}
  .back-mark__dot{width:110px;height:110px;border-radius:50%;background:var(--navy)}
  .back-mark__name{font-size:40px;font-weight:700;color:var(--lime);line-height:1}
  .back-web{position:absolute;left:0;right:0;top:300px;text-align:center;font-size:18px;letter-spacing:3px;color:var(--ink)}
</style>
</head>
<body>
  <section class="card card--front">
    <div class="brand">
      <span class="brand__dot"></span>
      <span class="brand__name">Borealis Thermal</span>
    </div>
    <p class="tagline">Builders of Ground-Source Heating for Cold Climates</p>
    <p class="person">Your Name, <span class="person__role">CEO</span></p>
    <ul class="contacts">
      <li><svg viewBox="0 0 16 16" aria-hidden="true"><path d="M3 1h3l1.5 4-2 1.2a9 9 0 0 0 4.3 4.3L11 8.5 15 10v3a2 2 0 0 1-2 2A12 12 0 0 1 1 3a2 2 0 0 1 2-2z"/></svg>(555) 014-2200</li>
      <li><svg viewBox="0 0 16 16" aria-hidden="true"><path d="M4 1h8v4H4zM1 6h14v6h-3v3H4v-3H1zm4 5v3h6v-3z"/></svg>(555) 014-2201</li>
      <li><svg viewBox="0 0 16 16" aria-hidden="true"><path d="M1 3h14v10H1zm1.5 1.2v.3L8 8.5l5.5-4v-.3z"/></svg>yourname@borealisthermal.com</li>
    </ul>
    <div class="web-band">www.borealisthermal.com</div>
    <p class="address">48 Lakeview Rd, Fairmont, MN 56000</p>
  </section>

  <section class="card card--back">
    <div class="back-mark">
      <span class="back-mark__dot"></span>
      <span class="back-mark__name">Borealis Thermal</span>
    </div>
    <p class="back-web">www.borealisthermal.com</p>
  </section>
</body>
</html>
```